A Maverick Business Card for a Maverick Company!

We're a maverick, 'rule breaker' market research company that needs a maverick business card design to suit who we are!

All logos, colours and text are detailed in the attached briefing document.

Note Please ignore the 'Look & Feel' wizard results and refer ONLY to the attached brief.

```html
<!DOCTYPE html>
<html lang="en">
<head>
<meta charset="utf-8">
<title>Clearlens Research – Business Card</title>
<link rel="stylesheet" href="https://fonts.googleapis.com/css2?family=Barlow:wght@400;500;600;700&display=swap">
<style>
  :root {
    --canvas: #e3e4e5;
    --red-top: #e5202a;
    --red-bottom: #b3121b;
    --red: #e31e26;
    --white: #ffffff;
    --grey-text: #555a5e;
    --card-shadow: 0 3px 10px rgba(0, 0, 0, 0.18);
  }
  * { box-sizing: border-box; margin: 0; padding: 0; }
  html, body {
    width: 1200px;
    height: 1200px;
    overflow: hidden;
    background: var(--canvas);
    font-family: "Barlow", sans-serif;
  }
  .stage { position: relative; width: 1200px; height: 1200px; }

  .card {
    position: absolute;
    left: 301px;
    width: 596px;
    height: 360px;
    border-radius: 18px;
    box-shadow: var(--card-shadow);
    overflow: hidden;
  }

  /* Front */
  .card--front {
    top: 216px;
    background: linear-gradient(180deg, var(--red-top) 0%, var(--red-bottom) 100%);
    color: var(--white);
  }
  .brand {
    position: absolute;
    left: 43px;
    top: 50px;
    display: flex;
    align-items: center;
    gap: 14px;
  }
  .brand__dot {
    width: 40px;
    height: 40px;
    border-radius: 50%;
    background: var(--white);
  }
  .brand__name {
    font-size: 34px;
    font-weight: 500;
    letter-spacing: 1px;
    color: var(--white);
  }
  .person {
    position: absolute;
    left: 43px;
    top: 190px;
  }
  .person__name { font-size: 21px; font-weight: 500; line-height: 1.2; }
  .person__title { font-size: 16px; font-weight: 400; line-height: 1.4; }
  .contact {
    position: absolute;
    left: 43px;
    top: 285px;
    font-size: 14px;
    line-height: 20px;
  }
  .contact b { font-weight: 700; }
  .contact__gap { margin-left: 8px; }

  /* Back */
  .card--back {
    top: 627px;
    background: var(--white);
  }
  .tagline {
    position: absolute;
    top: 60px;
    left: 0;
    width: 100%;
    text-align: center;
    color: var(--red);
    font-size: 25px;
    font-weight: 700;
    line-height: 32px;
  }
  .benefits {
    position: absolute;
    top: 168px;
    left: 0;
    width: 100%;
    list-style: none;
    color: var(--grey-text);
    font-size: 16px;
    line-height: 22px;
    text-align: center;
  }
  .benefits li { display: flex; justify-content: center; align-items: center; gap: 5px; }
  .benefits li:first-child { margin-left: -20px; }
  .tick { width: 16px; height: 14px; flex: none; }
  .address-band {
    position: absolute;
    top: 280px;
    left: 0;
    width: 100%;
    height: 30px;
    background: linear-gradient(180deg, var(--red-top), var(--red-bottom));
    color: var(--white);
    font-size: 14px;
    line-height: 30px;
    text-align: center;
  }
  .website {
    position: absolute;
    top: 322px;
    left: 0;
    width: 100%;
    text-align: center;
    color: var(--red);
    font-size: 14px;
  }
  .website b { font-weight: 700; }
</style>
</head>
<body>
<main class="stage">

  <section class="card card--front">
    <div class="brand">
      <span class="brand__dot"></span>
      <span class="brand__name">Clearlens Research</span>
    </div>
    <div class="person">
      <p class="person__name">Martin Keller</p>
      <p class="person__title">Managing Director</p>
    </div>
    <div class="contact">
      <p><b>Phone</b> 1300 555 214 <span class="contact__gap"><b>Direct</b> 0400 555 382</span></p>
      <p><b>Fax</b> 03 9555 0147 <span class="contact__gap"><b>Email</b> martin@clearlensresearch.com.au</span></p>
    </div>
  </section>

  <section class="card card--back">
    <h2 class="tagline">Clear answers, fast turnaround<br>and a fair, honest fee</h2>
    <ul class="benefits">
      <li><svg class="tick" viewBox="0 0 16 14"><path d="M1 7.5 L5.5 12 L15 2" fill="none" stroke="#e31e26" stroke-width="3" stroke-linecap="round" stroke-linejoin="round"/></svg>Custom market studies – focused, affordable and quick</li>
      <li><svg class="tick" viewBox="0 0 16 14"><path d="M1 7.5 L5.5 12 L15 2" fill="none" stroke="#e31e26" stroke-width="3" stroke-linecap="round" stroke-linejoin="round"/></svg>Base every business choice on solid evidence</li>
      <li><svg class="tick" viewBox="0 0 16 14"><path d="M1 7.5 L5.5 12 L15 2" fill="none" stroke="#e31e26" stroke-width="3" stroke-linecap="round" stroke-linejoin="round"/></svg>Send us your research question and we handle it all</li>
    </ul>
    <p class="address-band">Harbourside Business Suites, 48 Quayline Street, Melbourne Vic 3000</p>
    <p class="website">www.<b>clearlensresearch</b>.com.au</p>
  </section>

</main>
</body>
</html>
```